Web site for Tree Removal Company

What we are looking for:
-------------------------------
Looking for a wordpress web site, you can provide your own template or we can supply you with one (http://pelorin.vextura.com).

What we do
---------------
To see what we do please go to google Australia and google "Tree removal Sydney" or "Tree Removal Melbourne".

Web site requirements
-----------------------------
We prefer you to use our template as it has all our requirements in already.
- Responsive.
- Based on Wordpress.
- Full complaint and compatible with plugs.

Look, Feel and Appearance
------------------------------------
Please use the logo (see attached), for colour scheme, look and feel of the web site.

Thank you for your time and effort!

Target Market(s)

Tree Removal for Residential Homes

Industry/Entity Type

It Company

Number of Pages Required

4 page

Font styles to use
Serif
Sans Serif

Requirements
Must have
• Wordpress
Nice to have
• Original artwork, images and text
Should not have
• non related images or wording

```html
<!DOCTYPE html>
<html lang="en">
<head>
<meta charset="utf-8">
<title>Limbwise – Tree Lopping Services</title>
<link rel="stylesheet" href="https://fonts.googleapis.com/css2?family=Open+Sans:wght@400;600;700&display=swap">
<style>
:root{
  --green:#2dbb5a;
  --ink:#2b2b2b;
  --text:#555;
  --muted:#888;
  --grey-band:#d6d6d6;
  --footer:#4b4b4b;
  --footer-bottom:#3a3a3a;
  --white:#fff;
  --logo-bg:#1f2320;
}
*{box-sizing:border-box;margin:0;padding:0}
html,body{width:1200px;height:3046px;overflow:hidden}
body{font-family:"Open Sans",Arial,sans-serif;color:var(--text);background:var(--white);position:relative}

/* header */
.site-header{position:absolute;left:0;top:0;width:1200px;height:125px;background:var(--white);z-index:3}
.brand{position:absolute;left:0;top:0;width:330px;height:125px;background:var(--logo-bg);clip-path:polygon(0 0,100% 0,78% 100%,0 100%)}
.brand-mark{position:absolute;left:88px;top:30px;width:34px;height:34px;border-radius:50%;background:var(--green)}
.brand-name{position:absolute;left:62px;top:74px;font-size:18px;font-weight:600;color:var(--white);letter-spacing:1px}
.main-nav{position:absolute;right:50px;top:48px;display:flex;gap:46px;font-size:19px;color:var(--ink)}
.main-nav span{display:flex;align-items:center;gap:8px}
.main-nav svg{width:20px;height:20px;fill:var(--green)}

/* hero */
.hero{position:absolute;left:0;top:125px;width:1200px;height:423px;background:linear-gradient(90deg,#6b4a34 0%,#8a5a3a 25%,#4e3a2c 50%,#9a5a36 75%,#5d3f2c 100%)}
.hero::after{content:"";position:absolute;inset:0;background:rgba(0,0,0,.35)}
.hero-strip{position:absolute;left:0;top:548px;width:1200px;height:12px;background:var(--green)}
.hero-copy{position:absolute;left:0;top:238px;width:1200px;text-align:center;color:var(--white);z-index:2}
.hero-copy .lead{font-size:37px;font-weight:400;letter-spacing:.5px}
.hero-copy .strong{font-size:40px;font-weight:700;letter-spacing:1.5px;margin-top:2px}
.btn{display:inline-block;background:var(--green);color:var(--white);font-size:22px;text-align:center}
.hero-btn{position:absolute;left:481px;top:368px;width:274px;height:42px;line-height:42px;z-index:2}
.slide-arrow{position:absolute;top:295px;width:32px;height:40px;background:rgba(0,0,0,.55);z-index:2}
.slide-arrow svg{width:32px;height:40px;stroke:var(--white);fill:none;stroke-width:3}

/* features */
.feature{position:absolute;top:630px;width:230px;text-align:center}
.feature svg{width:52px;height:52px;fill:var(--ink)}
.feature h3{font-size:25px;font-weight:400;color:var(--ink);margin:14px 0 8px;letter-spacing:.5px}
.feature p{font-size:14px;line-height:19px;color:var(--text)}

/* tree services */
.services-gallery{position:absolute;left:0;top:886px;width:1200px;height:445px;background:radial-gradient(ellipse at 50% 40%,#6d6a66 0%,#3d3a37 55%,#2a2826 100%)}
.services-gallery h2{position:absolute;top:24px;width:100%;text-align:center;color:var(--white);font-size:38px;font-weight:400;letter-spacing:1px}
.thumb{position:absolute;width:213px;height:125px;border:3px solid var(--white)}

/* accordion */
.accordion-open{position:absolute;left:61px;top:1404px;width:533px;height:222px;border:1px solid #ddd;background:#f3f3f3}
.accordion-open h4{font-size:16px;font-weight:700;color:var(--ink);padding:10px 18px;border-bottom:1px solid #e3e3e3;background:var(--white)}
.accordion-open p{font-size:15px;line-height:21px;color:var(--muted);padding:14px 18px 0 36px}
.accordion-item{position:absolute;left:61px;width:533px;height:42px;border:1px solid #ddd;background:var(--white);font-size:15px;color:var(--ink);padding:10px 18px 0 18px}
.accordion-item::before{content:"▸ ";color:var(--muted)}
.safety h4{position:absolute;left:626px;top:1408px;font-size:16px;font-weight:700;color:var(--ink)}
.safety p{position:absolute;left:626px;top:1440px;width:510px;font-size:14px;line-height:19px;color:var(--muted)}
.carousel{position:absolute;left:626px;top:1605px;width:510px;height:125px;border:1px solid #e2e2e2}
.carousel .nav{position:absolute;top:40px;width:24px;height:40px}
.carousel .nav svg{width:24px;height:40px;stroke:var(--green);fill:none;stroke-width:3}
.carousel .pic{position:absolute;top:8px;width:120px;height:108px}

/* services grey */
.service-band{position:absolute;left:0;top:1788px;width:1200px;height:482px;background:var(--grey-band)}
.service{position:absolute;width:520px}
.service .icon{position:absolute;left:0;top:0;width:64px;height:64px;border-radius:50%;background:var(--ink)}
.service .icon svg{width:64px;height:64px;fill:var(--white)}
.service h3{position:absolute;left:90px;top:12px;font-size:32px;font-weight:700;color:var(--ink)}
.service p{position:absolute;left:-18px;top:70px;width:520px;font-size:14px;line-height:19px;color:#444}

/* testimonial */
.testimonial{position:absolute;left:0;top:2270px;width:1200px;height:320px;background:linear-gradient(180deg,#5d6b56 0%,#7a8670 45%,#4f5a48 100%)}
.testimonial h2{position:absolute;top:50px;width:100%;text-align:center;color:var(--white);font-size:34px;font-weight:700}
.testimonial blockquote{position:absolute;left:300px;top:116px;width:600px;text-align:center;color:var(--white);font-size:22px;line-height:28px}
.quote-mark{position:absolute;color:rgba(255,255,255,.85);font-family:Georgia,serif;font-size:130px;line-height:1}
.testimonial .btn{position:absolute;left:527px;top:242px;width:173px;height:43px;line-height:43px;font-size:23px}

/* footer */
.site-footer{position:absolute;left:0;top:2590px;width:1200px;height:410px;background:var(--footer);color:var(--white)}
.site-footer h5{position:absolute;font-size:20px;font-weight:700}
.footer-about{position:absolute;left:67px;top:58px;width:252px;font-size:13.5px;line-height:17px;font-weight:600;color:#e6e6e6}
.footer-list{position:absolute;list-style:none;font-size:13px;color:#e6e6e6}
.footer-list li{height:32px;padding-top:8px}
.footer-list li::before{content:"› ";color:var(--white)}
.footer-quote{position:absolute;left:862px;top:50px;width:260px;font-size:16px;line-height:20px;color:#e6e6e6}
.post-image{position:absolute;left:871px;top:267px;width:235px;height:113px;background:linear-gradient(135deg,#5a5a4e,#8b7d55 50%,#3e4634)}
.footer-bottom{position:absolute;left:0;top:3000px;width:1200px;height:46px;background:var(--footer-bottom);color:#ddd;font-size:14px;padding:14px 0 0 60px}
</style>
</head>
<body>

<header class="site-header">
  <div class="brand"><span class="brand-mark"></span><span class="brand-name">LIMBWISE</span></div>
  <nav class="main-nav">
    <span><svg viewBox="0 0 20 20"><path d="M10 2 1 10h3v8h5v-5h2v5h5v-8h3z"/></svg>Home</span>
    <span><svg viewBox="0 0 20 20"><path d="M10 1 3 11h4l-3 5h5v3h2v-3h5l-3-5h4z"/></svg>Tree Services</span>
    <span><svg viewBox="0 0 20 20"><path d="M10 1 2 4v6c0 5 4 8 8 9 4-1 8-4 8-9V4z"/></svg>Safety</span>
    <span><svg viewBox="0 0 20 20"><circle cx="10" cy="10" r="9"/></svg>FAQs</span>
    <span><svg viewBox="0 0 20 20"><path d="M4 1h4l2 5-3 2c1 2 3 4 5 5l2-3 5 2v4c0 1-1 3-3 3C8 19 1 12 1 4c0-2 2-3 3-3z"/></svg>Call us today on 02 5550 1934</span>
  </nav>
</header>

<section class="hero" role="img" aria-label="Photo of freshly cut tree logs stacked in a yard"></section>
<div class="slide-arrow" style="left:0"><svg viewBox="0 0 32 40"><path d="M20 12 12 20l8 8"/></svg></div>
<div class="slide-arrow" style="right:0"><svg viewBox="0 0 32 40"><path d="M12 12l8 8-8 8"/></svg></div>
<div class="hero-copy">
  <p class="lead">Our aim for the business has always been to provide</p>
  <p class="strong">FAST, RELIABLE TREE LOPPING SERVICES</p>
</div>
<a class="btn hero-btn">Read More</a>
<div class="hero-strip"></div>

<section class="features">
  <div class="feature" style="left:104px">
    <svg viewBox="0 0 52 52"><path d="M6 44 34 16l4 4L10 48z"/><path d="M38 4l2 5 5 2-5 2-2 5-2-5-5-2 5-2z"/></svg>
    <h3>Ethical</h3>
    <p>We actively refuse to remove trees illegally. This saves you from hefty fines from your council</p>
  </div>
  <div class="feature" style="left:363px">
    <svg viewBox="0 0 52 52"><circle cx="20" cy="30" r="12"/><circle cx="20" cy="30" r="4" fill="#fff"/><circle cx="39" cy="14" r="8"/><circle cx="39" cy="14" r="3" fill="#fff"/></svg>
    <h3>Affordable</h3>
    <p>As a small business our aim is to provide tree services by qualified arborists at affordable</p>
  </div>
  <div class="feature" style="left:616px">
    <svg viewBox="0 0 52 52"><rect x="4" y="6" width="10" height="10"/><rect x="18" y="6" width="30" height="10"/><rect x="4" y="21" width="10" height="10"/><rect x="18" y="21" width="30" height="10"/><rect x="4" y="36" width="10" height="10"/><rect x="18" y="36" width="30" height="10"/></svg>
    <h3>Free Mulch</h3>
    <p>Some customers prefer us to turn their trees into fire wood or mulch, this can keep you</p>
  </div>
  <div class="feature" style="left:875px">
    <svg viewBox="0 0 52 52"><path d="M4 4h14l-5 5 9 9-4 4-9-9-5 5zM48 4v14l-5-5-9 9-4-4 9-9-5-5zM4 48V34l5 5 9-9 4 4-9 9 5 5zM48 48H34l5-5-9-9 4-4 9 9 5-5z"/></svg>
    <h3>Land Cleaning</h3>
    <p>Our team specialise in clearing and grubbing land for construction projects.</p>
  </div>
</section>

<section class="services-gallery" role="img" aria-label="Blurred photo of a forest backdrop">
  <h2>Tree Services</h2>
  <div class="thumb" style="left:204px;top:95px;background:linear-gradient(135deg,#6f7c5a,#b9b7a6)" role="img" aria-label="Arborist cutting a fallen trunk"></div>
  <div class="thumb" style="left:506px;top:95px;background:linear-gradient(135deg,#4c5a3a,#8a8f6b)" role="img" aria-label="Climber working high in a tree"></div>
  <div class="thumb" style="left:807px;top:95px;background:linear-gradient(135deg,#687a5c,#a5ad8f)" role="img" aria-label="Tall trees beside a house"></div>
  <div class="thumb" style="left:204px;top:287px;background:linear-gradient(135deg,#3d3a30,#c56a2a)" role="img" aria-label="Chainsaw cutting a log"></div>
  <div class="thumb" style="left:506px;top:287px;background:linear-gradient(135deg,#5a6b46,#9ba07a)" role="img" aria-label="Crew removing a tree in a garden"></div>
  <div class="thumb" style="left:807px;top:287px;background:linear-gradient(135deg,#a7764a,#d6a574)" role="img" aria-label="Cross sections of cut logs"></div>
</section>

<div class="accordion-open">
  <h4>The Arbor Process</h4>
  <p>1. Identify any trees, palms, branches, stumps that require removal and/or pruning and record their details. Information like species, whether it is dead or alive, and the height, will be required in any applications required by your local council. Some trees can be removed without application...</p>
</div>
<div class="accordion-item" style="top:1638px">The Harrow Tree Legacy</div>
<div class="accordion-item" style="top:1690px">The Harrow Institute</div>
<div class="safety">
  <h4>MORE THAN SAFETY GEAR.</h4>
  <p>We implement safety controls that are more than personal protective equipment (PPE). Our first method for reducing risk is by eliminating it. If we can do the work in a different (safer) way then we will charge our practices to suit the job. If it is a risk that cannot be eliminated, we work with it by using administrative or engineering restrictions. Our last defence is our ever-present PPE – our helmets, harnesses, shoes, gloves, glasses, and high-visibility vests.</p>
</div>
<div class="carousel">
  <div class="nav" style="left:12px"><svg viewBox="0 0 24 40"><path d="M16 12 8 20l8 8"/></svg></div>
  <div class="pic" style="left:60px;background:linear-gradient(135deg,#4f5c3c,#8e8f70)" role="img" aria-label="Tree pruning job"></div>
  <div class="pic" style="left:190px;background:linear-gradient(135deg,#56654a,#a0a48a)" role="img" aria-label="Truck loaded with branches"></div>
  <div class="pic" style="left:315px;background:linear-gradient(135deg,#6a7656,#b3b49c)" role="img" aria-label="Arborist in a tree"></div>
  <div class="nav" style="right:12px"><svg viewBox="0 0 24 40"><path d="M8 12l8 8-8 8"/></svg></div>
</div>

<section class="service-band">
  <div class="service" style="left:91px;top:58px">
    <div class="icon"><svg viewBox="0 0 64 64"><path d="M32 12 20 32h8l-8 12h24l-8-12h8z"/><rect x="30" y="44" width="4" height="8"/></svg></div>
    <h3>TREE REMOVAL</h3>
    <p>Mulching is the most beneficial thing a home owner can do for the health of a young tree. Mulches are materials placed on the soil surface to improve soil structure, oxygen levels, temperature and moisture availability. Properly applied, mulch can give landscapes a handsome, well-groomed appearance.</p>
  </div>
  <div class="service" style="left:664px;top:58px">
    <div class="icon"><svg viewBox="0 0 64 64"><circle cx="24" cy="40" r="7"/><circle cx="40" cy="40" r="7"/><path d="M27 34 40 14l3 2-12 20zM37 34 24 14l-3 2 12 20z"/></svg></div>
    <h3>PRUNING</h3>
    <p>We prune to remove diseased, damaged or dead material on plants. Pruning is a horticultural practice involving the selective removal of parts of a plant, such as branches, buds, or roots. It will help your garden trees yield high and capable of growing strong and healthy.</p>
  </div>
  <div class="service" style="left:91px;top:222px">
    <div class="icon"><svg viewBox="0 0 64 64"><ellipse cx="32" cy="28" rx="14" ry="6"/><path d="M18 28v10c0 3 6 6 14 6s14-3 14-6V28z"/></svg></div>
    <h3>STUMP GRINDING</h3>
    <p>We offer a wide range of hedging suitable for formal, small compact or larger hedges and screens. We provide large and small hedges that are suitable for your garden and living environment.</p>
  </div>
  <div class="service" style="left:664px;top:222px">
    <div class="icon"><svg viewBox="0 0 64 64"><path d="M12 44h40l-6-10H18z"/><path d="M24 34 32 18l8 16z"/></svg></div>
    <h3>LAND CLEARING</h3>
    <p>The best and safest way to remove a tree stump is by grinding both the stump itself and the tree roots below it. We specialise in stump grinding with modern equipment that can access the most difficult areas to remove those unwanted stumps. Our company is dedicated to providing superior customer service and top quality tree care.</p>
  </div>
</section>

<section class="testimonial" role="img" aria-label="Blurred photo of green trees">
  <h2>What People Say About Us</h2>
  <span class="quote-mark" style="left:225px;top:96px">“</span>
  <blockquote>I would like to say how good, willing and helpful Dorian and his mate were. It was more difficult that he originally thought but they did an excellent job and even cleared up..... something I usually have to do!!!! — Maren</blockquote>
  <span class="quote-mark" style="left:912px;top:212px">”</span>
  <a class="btn">Read More</a>
</section>

<footer class="site-footer">
  <h5 style="left:67px;top:18px">About Us</h5>
  <p class="footer-about">This is the short story of our crew. Since day one we have cared for the trees of local homes, from careful pruning to full removal and clean up. Our arborists are trained, insured and proud of tidy work. We treat every yard like our own, leave no mess behind and always give honest advice about what a tree really needs. Call us for a free quote and a friendly chat today.</p>
  <h5 style="left:347px;top:18px">Main Menu</h5>
  <ul class="footer-list" style="left:347px;top:60px">
    <li>Home</li><li>Tree Removal Services Sydney</li><li>Tree Surgery Sydney</li><li>Tree Reports</li><li>FAQs</li><li>Contact Us</li>
  </ul>
  <h5 style="left:612px;top:18px">Our Services</h5>
  <ul class="footer-list" style="left:612px;top:60px">
    <li>Tree Removal</li><li>Tree Mulching</li><li>Pruning</li><li>Hedging</li><li>Stump Grinding</li><li>Arborists Reports</li><li>Strata Management</li>
  </ul>
  <h5 style="left:862px;top:18px">What People Say About Us</h5>
  <p class="footer-quote">" I would like to say how good, willing and helpful Dorian and his mate were. It was more difficult that he originally thought but they did an excellent job and even cleared up..... something I usually have to do!!!! " – Maren</p>
  <h5 style="left:871px;top:226px">Post Images</h5>
  <div class="post-image" role="img" aria-label="Arborist cutting branches with a chainsaw"></div>
</footer>
<div class="footer-bottom">© 2015 Limbwise</div>

</body>
</html>
```